Need Business Cards for my Business

email address: rkpmarlowhollowworks@vendrimail.com
web address: rkpmarlowhollowworks.net
Slogan: We offer various QVN licenses
Rowland K. Pemberly
Please stick with colors of Company Logo
would like the card to be more of the color example of the logo.
If you need PDF copy of logo email me at the above account.
Creative control rests with you.

Industry/Entity Type

Business

Contact Information for Business Card

I am a minimalist, but would like something to pop and stand out amongst other cards, make it memorable.

Font styles to use
Serif
Decorative
Script

```html
<!DOCTYPE html>
<html lang="en">
<head>
<meta charset="utf-8">
<title>RKP Marlow Testing – Business Cards</title>
<link href="https://fonts.googleapis.com/css2?family=Arimo:wght@400;700&display=swap" rel="stylesheet">
<style>
  :root {
    --stage: #3b3e43;
    --card-white: #ffffff;
    --brand-blue: #1d4f8e;
    --blue-deep: #163f75;
    --blue-light: #2a64a8;
    --brand-red: #d8232e;
    --red-light: #e8414a;
    --text-white: #ffffff;
    --text-soft: #dbe6f4;
  }
  * { box-sizing: border-box; margin: 0; padding: 0; }
  html, body {
    width: 1200px; height: 950px; overflow: hidden;
    background: var(--stage);
    font-family: "Arimo", Arial, sans-serif;
  }
  .stage {
    position: relative; width: 1200px; height: 950px;
  }
  .card {
    position: absolute; left: 215px;
    width: 770px; height: 440px;
    border-radius: 4px; overflow: hidden;
    box-shadow: 0 10px 30px rgba(0,0,0,.35);
  }

  /* Back of card */
  .card-back {
    top: 25px;
    background: linear-gradient(135deg, var(--blue-light) 0%, var(--brand-blue) 45%, var(--blue-deep) 100%);
    color: var(--text-white);
  }
  .card-back .wordmark {
    position: absolute; top: 92px; left: 0; right: 0;
    display: flex; justify-content: center; align-items: center; gap: 16px;
  }
  .card-back .wordmark-mark {
    width: 26px; height: 26px; background: var(--text-white);
  }
  .card-back .wordmark-name {
    font-weight: 700; font-size: 44px; letter-spacing: 2px; color: var(--text-white);
  }
  .card-back .slogan {
    position: absolute; top: 178px; left: 0; right: 0;
    text-align: center; font-weight: 700; font-size: 22px;
  }
  .card-back .license-list {
    position: absolute; top: 232px; left: 60px; right: 60px;
    list-style: none; text-align: center;
    font-size: 19px; line-height: 1.75; color: var(--text-soft);
  }

  /* Front of card */
  .card-front {
    top: 485px; background: var(--card-white);
  }
  .card-front .wordmark {
    position: absolute; top: 0; left: 0; right: 0; height: 228px;
    display: flex; justify-content: center; align-items: center; gap: 16px;
  }
  .card-front .wordmark-mark {
    width: 26px; height: 26px; background: var(--brand-red);
  }
  .card-front .wordmark-name {
    font-weight: 700; font-size: 44px; letter-spacing: 2px; color: var(--brand-blue);
  }
  .name-band {
    position: absolute; top: 228px; left: 0; right: 0; height: 88px;
    background: linear-gradient(90deg, var(--brand-red), var(--red-light) 60%, var(--brand-red));
    color: var(--text-white); text-align: center;
    display: flex; flex-direction: column; justify-content: center;
  }
  .name-band .person-name { font-size: 28px; letter-spacing: .5px; }
  .name-band .person-role { font-size: 17px; margin-top: 4px; }
  .divider {
    position: absolute; top: 316px; left: 0; right: 0; height: 4px;
    background: var(--card-white);
  }
  .contact-band {
    position: absolute; top: 320px; left: 0; right: 0; bottom: 0;
    background: linear-gradient(135deg, var(--blue-light), var(--brand-blue) 50%, var(--blue-deep));
    color: var(--text-white); font-size: 18px; text-align: center;
    display: flex; flex-direction: column; justify-content: center; gap: 12px;
  }
  .contact-line span + span { margin-left: 22px; }
</style>
</head>
<body>
<main class="stage">

  <section class="card card-back" aria-label="Back of business card">
    <div class="wordmark">
      <span class="wordmark-mark"></span>
      <span class="wordmark-name">RKP MARLOW TESTING</span>
    </div>
    <p class="slogan">We offer various QVN licenses</p>
    <ul class="license-list">
      <li>Radiotelephone Operator License • GMDSS Radio Operators License</li>
      <li>Marine Radio Operator Permit • Ship Radar Endorsement</li>
      <li>Restricted Radiotelephone Operator License</li>
    </ul>
  </section>

  <section class="card card-front" aria-label="Front of business card">
    <div class="wordmark">
      <span class="wordmark-mark"></span>
      <span class="wordmark-name">RKP MARLOW TESTING</span>
    </div>
    <div class="name-band">
      <p class="person-name">Rowland K. Pemberly</p>
      <p class="person-role">CEO/Founder</p>
    </div>
    <div class="divider"></div>
    <div class="contact-band">
      <p class="contact-line"><span>P : 555-014-2276</span><span>M : 555 019 4803</span></p>
      <p class="contact-line"><span>E : rkpmarlowhollowworks@vendrimail.com</span><span>W : rkpmarlowhollowworks.net</span></p>
    </div>
  </section>

</main>
</body>
</html>
```